Business card design needed

A business card and logo for my energy healing practice Tarrawong's Healing Spring. It should match my website www.tarrawongshealingspring.com in colours and atmosphere. It should look at bit rustic in combination with nature linking in with the natural healing techniques I offer in a heritage country town in NSW Australia. My business also includes a directory of other health and healing practitioners 'The Spring'. It would be nice if a graphic impression of the attached picture of the water feature in my front yard can be used.

Industry/Entity Type

Health

Contact Information for Business Card

Tarrawong's Healing Spring, Felicity Haldane, 41 Carrick St, Tarrawong NSW 2735, M. 0431 596 018, info@tarrawongshealingspring.com, www.tarrawongshealingspring.com,
Gentle Energy Work - Rooted In Country
Facebook/Twitter see Lakeside Mending

```html
<!DOCTYPE html>
<html lang="en">
<head>
<meta charset="utf-8">
<title>Tarrawong's Healing Spring – Business Card</title>
<link href="https://fonts.googleapis.com/css2?family=Fira+Sans:wght@300;400&family=Fira+Sans+Condensed:wght@400&family=Parisienne&display=swap" rel="stylesheet">
<style>
  :root {
    --ink-dark: #0c1a20;
    --teal-deep: #173038;
    --teal-mid: #2a5a64;
    --teal-bright: #3c7480;
    --brand-ink: #2c474e;
    --card-text: #eef3f4;
  }
  html, body {
    margin: 0;
    padding: 0;
    width: 1200px;
    height: 693px;
    overflow: hidden;
    background: #ffffff;
  }
  .card {
    position: relative;
    width: 1200px;
    height: 693px;
    overflow: hidden;
    background: linear-gradient(160deg, var(--ink-dark) 0%, var(--teal-deep) 40%, var(--teal-mid) 78%, var(--teal-bright) 100%);
    font-family: "Fira Sans", sans-serif;
  }
  .garden-scene {
    position: absolute;
    inset: 0;
    width: 1200px;
    height: 693px;
  }
  .brand {
    position: absolute;
    left: 66px;
    top: 392px;
    color: var(--brand-ink);
  }
  .brand-name {
    font-family: "Fira Sans", sans-serif;
    font-weight: 300;
    font-size: 72px;
    line-height: 90px;
    margin: 0;
  }
  .brand-tagline {
    font-family: "Fira Sans Condensed", sans-serif;
    font-size: 26px;
    letter-spacing: 0.4px;
    margin: 10px 0 0 2px;
  }
  .practitioner {
    position: absolute;
    left: 652px;
    top: 62px;
    margin: 0;
    font-family: "Parisienne", cursive;
    font-weight: 400;
    font-size: 72px;
    line-height: 88px;
    color: var(--card-text);
  }
  .contact {
    position: absolute;
    left: 655px;
    top: 262px;
    margin: 0;
    padding: 0;
    list-style: none;
    color: var(--card-text);
    font-size: 29px;
    line-height: 46px;
    letter-spacing: 0.4px;
  }
  .social {
    position: absolute;
    left: 655px;
    top: 494px;
    margin: 0;
    padding: 0;
    list-style: none;
    color: var(--card-text);
    font-size: 29px;
    line-height: 47px;
  }
  .social li {
    display: flex;
    align-items: center;
  }
  .social-dot {
    width: 34px;
    height: 34px;
    border-radius: 50%;
    background: var(--card-text);
    margin-right: 20px;
    flex: none;
  }
</style>
</head>
<body>
  <div class="card">
    <svg class="garden-scene" viewBox="0 0 1200 693" role="img" aria-label="Soft-toned photograph of a garden with a stone bird bath water feature in front of a country cottage">
      <defs>
        <linearGradient id="scene-tone" x1="0" y1="0" x2="0.25" y2="1">
          <stop offset="0" stop-color="#3f5a61"/>
          <stop offset="0.45" stop-color="#7f989e"/>
          <stop offset="0.75" stop-color="#bccbcf"/>
          <stop offset="1" stop-color="#dde6e8"/>
        </linearGradient>
      </defs>
      <path fill="url(#scene-tone)" d="M0 0 H598 L604 40 L596 78 L609 120 L601 168 L614 210 L606 258 L620 300 L612 346 L626 392 L617 436 L631 480 L622 528 L636 572 L628 620 L640 660 L634 693 H0 Z"/>
    </svg>

    <div class="brand">
      <p class="brand-name">Tarrawong's<br>Healing Spring</p>
      <p class="brand-tagline">GENTLE ENERGY WORK - ROOTED IN COUNTRY</p>
    </div>

    <h1 class="practitioner">Felicity<br>Haldane</h1>

    <ul class="contact">
      <li>41 Carrick Street</li>
      <li>Tarrawong NSW 2735</li>
      <li>0431 596 018</li>
      <li>info@tarrawongshealingspring.com</li>
      <li>www.tarrawongshealingspring.com</li>
    </ul>

    <ul class="social">
      <li><span class="social-dot"></span>lakesidemending</li>
      <li><span class="social-dot"></span>@lakesidemending</li>
      <li><span class="social-dot"></span>lakesidemending</li>
    </ul>
  </div>
</body>
</html>
```